Design a stunning business card

Needed a trendy business card. Here are the details for the front and back. The logo is also attached. I will award the contest as soon as I find a cool design. Thanks for your interest in the contest and your creativity!

FRONT:
LM Craft Works
-Remodeling, Remediation and Restoration
-General contractors
-Licensed, Bonded and Insured

Mobile: 202-555-0147
Fax: 202-555-0183
Toll-free: 1-833-555-0162
Email: Service@lmCraftWorks.example
4870 R ST NW, #210, Washington, DC 20007
***Suggested for front is company logo attached

BACK:
We are hiring! Estamos contratando!
Master Carpenters, Drywall Installers, Construction Foreman
Call: 202-555-0147

***Suggested for back are logos of NestFinder , BVQ Certified Firm and Watt Badge

```html
<!DOCTYPE html>
<html lang="en">
<head>
<meta charset="utf-8">
<title>LM Craft Works – Business Card</title>
<link href="https://fonts.googleapis.com/css2?family=Lato:wght@400;700;900&display=swap" rel="stylesheet">
<style>
  :root {
    --backdrop: #676b70;
    --brand-blue: #2a93c0;
    --brand-blue-dark: #1f7aa3;
    --ink: #2b2f33;
    --ink-soft: #555b61;
    --paper: #ffffff;
  }
  * { box-sizing: border-box; margin: 0; padding: 0; }
  html, body { width: 1200px; height: 773px; overflow: hidden; }
  body {
    background: var(--backdrop);
    font-family: "Lato", sans-serif;
    display: flex;
    align-items: center;
    justify-content: center;
    gap: 40px;
  }
  .card {
    width: 540px;
    height: 309px;
    position: relative;
    box-shadow: 0 6px 18px rgba(0,0,0,.3);
  }

  /* Front */
  .card-front {
    background: var(--paper);
    border: 8px solid var(--brand-blue);
    padding: 16px 24px;
    color: var(--ink);
  }
  .brand { display: flex; align-items: center; gap: 10px; }
  .brand-dot {
    width: 30px; height: 30px; border-radius: 50%;
    background: var(--brand-blue);
  }
  .brand-name { font-size: 22px; font-weight: 700; color: var(--brand-blue); }
  .services { list-style: none; margin: 6px 0 0 40px; }
  .services li {
    font-size: 11px; color: var(--ink-soft); line-height: 15px;
    display: flex; align-items: center; gap: 6px;
  }
  .services li::before {
    content: ""; width: 0; height: 0;
    border-left: 5px solid var(--ink); border-top: 3px solid transparent; border-bottom: 3px solid transparent;
  }
  .divider-curve { display: block; width: 300px; height: 14px; margin: 4px 0 2px 0; }
  .person-name { font-size: 21px; font-weight: 900; letter-spacing: .5px; }
  .person-title { font-size: 11px; font-weight: 700; color: var(--brand-blue); margin-top: 1px; }
  .contact { list-style: none; margin-top: 8px; }
  .contact li {
    font-size: 10.5px; color: var(--ink-soft); line-height: 14.5px;
    display: flex; align-items: center; gap: 7px;
  }
  .contact svg { width: 10px; height: 10px; flex: none; fill: var(--ink); }
  .contact .note { color: var(--brand-blue); }

  /* Back */
  .card-back {
    background: var(--brand-blue);
    border: 8px solid var(--paper);
    color: var(--paper);
    padding: 22px 26px;
  }
  .hiring-title { font-size: 20px; font-weight: 900; }
  .roles { list-style: none; display: flex; gap: 14px; margin-top: 6px; }
  .roles li { font-size: 11px; display: flex; align-items: center; gap: 4px; }
  .roles svg { width: 10px; height: 10px; stroke: var(--paper); fill: none; stroke-width: 2; }
  .call-line { font-size: 30px; font-weight: 900; margin-top: 22px; }
  .badges { position: absolute; right: 30px; top: 116px; display: flex; gap: 12px; }
  .badge { width: 50px; height: 50px; border-radius: 50%; background: #e8eef1; border: 3px solid var(--paper); }
  .badge-square { border-radius: 6px; background: var(--brand-blue-dark); }
  .division-note { position: absolute; left: 0; right: 0; bottom: 18px; text-align: center; font-size: 12px; }
</style>
</head>
<body>

<section class="card card-front" aria-label="Business card front">
  <div class="brand">
    <span class="brand-dot"></span>
    <span class="brand-name">LM Craft Works</span>
  </div>
  <ul class="services">
    <li>Remodeling, Remediation and Restoration</li>
    <li>General Contractors</li>
    <li>Licensed, Bonded and Insured</li>
  </ul>
  <svg class="divider-curve" viewBox="0 0 300 14" aria-hidden="true">
    <path d="M2 12 Q150 -6 298 12 Q150 2 2 12 Z" fill="var(--brand-blue)"/>
  </svg>
  <h1 class="person-name">DANE MORROW</h1>
  <p class="person-title">Managing Member/CEO</p>
  <ul class="contact">
    <li><svg viewBox="0 0 10 10"><path d="M5 0a3.5 3.5 0 0 0-3.5 3.5C1.5 6 5 10 5 10s3.5-4 3.5-6.5A3.5 3.5 0 0 0 5 0zm0 5a1.5 1.5 0 1 1 0-3 1.5 1.5 0 0 1 0 3z"/></svg>4870 R ST NW, #210, Washington, DC 20007</li>
    <li><svg viewBox="0 0 10 10"><rect x="2.5" y="0" width="5" height="10" rx="1"/></svg>202-555-0147</li>
    <li><svg viewBox="0 0 10 10"><path d="M2 1l2 2-1 1.5c.8 1.5 1.8 2.5 3.3 3.3L7.8 6.8 10 8.8 8.5 10C4 9.5.5 6 0 1.5z"/></svg>1-833-555-0162 <span class="note">(Toll free)</span></li>
    <li><svg viewBox="0 0 10 10"><rect x="0" y="3" width="10" height="5" rx="1"/><rect x="2" y="0" width="6" height="3"/></svg>202-555-0183</li>
    <li><svg viewBox="0 0 10 10"><path d="M0 2h10v6H0z"/><path d="M0 2l5 3.5L10 2" stroke="#fff" stroke-width="1" fill="none"/></svg>Service@lmCraftWorks.example</li>
    <li><svg viewBox="0 0 10 10"><circle cx="5" cy="5" r="5"/><path d="M0 5h10M5 0c-2 3-2 7 0 10M5 0c2 3 2 7 0 10" stroke="#fff" stroke-width=".8" fill="none"/></svg>lmCraftWorks.example</li>
  </ul>
</section>

<section class="card card-back" aria-label="Business card back">
  <h2 class="hiring-title">We are hiring! Estamos contratando!</h2>
  <ul class="roles">
    <li><svg viewBox="0 0 10 10"><path d="M1 5l3 3 5-7"/></svg>Master Carpenters</li>
    <li><svg viewBox="0 0 10 10"><path d="M1 5l3 3 5-7"/></svg>Drywall Installers</li>
    <li><svg viewBox="0 0 10 10"><path d="M1 5l3 3 5-7"/></svg>Construction Foreman</li>
  </ul>
  <p class="call-line">Call: 202-555-0147</p>
  <div class="badges">
    <span class="badge badge-square" role="img" aria-label="Watt Badge certification mark"></span>
    <span class="badge" role="img" aria-label="BVQ Certified Firm badge"></span>
    <span class="badge" role="img" aria-label="NestFinder approved badge"></span>
  </div>
  <p class="division-note">LM Craft Works is a division of Keystone Alliance LLC</p>
</section>

</body>
</html>
```